Pine Ridge Traders, LLC- Global Beverage Company with 100% Cold Chain Logistics

Hey All, My Name is Dale, I am a young business owner in a competitive export space, but my niche is that I am shipping all of my beer around the world, "100% Cold Chain". This model is more costly, but it protects the integrity of the beer itself and will give folks in foreign countries the best representation of what US Craft Beer has to offer.

I am not a branding guy and don't claim to be one, I am a salesperson first, and will be referring to all of you to create something great that will be memorable.

I am looking for a basic Business Card Design for my Craft Beer Export company. I sell US Craft Beer in several countries around the globe. Austrailia, China, Taiwan, Chile, France, New Zealand... to name a few.

I am looking for a sleek, modern, and fresh design. Quickly!

Thanks for your consideration!

Cheers,

Dale

Target Market(s)

International

Contact Information for Business Card

Dale Corwin
Founder- Roving Hops Guy
Dale@PineRidgeTraders.example
@RovingHopsGuy- Instagram only
www.Pineridgetraders.example
@PineRidgeTradersAU- Instagram Only

Font styles to use
Serif

Colors
0592cd
ffffff

Requirements
Must have
• Name-
• Title-
• Email-
• Social Media Handle-
• Company Website-
Nice to have
• Nice Logo/ Images on Card
Should not have
• Tacky Beer Images

```html
<!DOCTYPE html>
<html lang="en">
<head>
<meta charset="utf-8">
<title>Roving Hops Guy – Business Card</title>
<link rel="stylesheet" href="https://fonts.googleapis.com/css2?family=Barlow+Condensed:wght@500;600;700&family=Quicksand:wght@400&display=swap">
<style>
  :root {
    --page-bg: #ffffff;
    --card-light: #f5f5f5;
    --card-mid: #e4e4e4;
    --ink: #5b5b5b;
    --ink-soft: #6a6a6a;
    --dark-band: #2b2b2b;
    --dark-band-2: #4a4a4a;
    --gold-1: #ffcc1f;
    --gold-2: #f29a00;
    --gold-3: #d96a00;
    --shade: #d6d6d6;
    --icon: #5f5f5f;
  }
  html, body {
    margin: 0;
    padding: 0;
    width: 1200px;
    height: 706px;
    overflow: hidden;
    background: var(--page-bg);
  }
  .canvas {
    position: relative;
    width: 1200px;
    height: 706px;
  }
  .side-label {
    position: absolute;
    left: 240px;
    width: 90px;
    text-align: center;
    font-family: "Barlow Condensed", sans-serif;
    font-weight: 600;
    font-size: 30px;
    color: var(--ink);
    line-height: 1;
    letter-spacing: 0.5px;
  }
  .side-label--back { top: 149px; }
  .side-label--front { top: 500px; }
  .card {
    position: absolute;
    left: 374px;
    width: 558px;
    height: 309px;
    background: linear-gradient(135deg, var(--card-light) 0%, #ececec 60%, var(--card-mid) 100%);
    box-shadow: 0 14px 22px rgba(0,0,0,0.18), 0 0 1px rgba(0,0,0,0.35);
    overflow: hidden;
  }
  .card--back { top: 14px; }
  .card--front { top: 371px; }
  .card svg.card-shapes {
    position: absolute;
    left: 0;
    top: 0;
    width: 558px;
    height: 309px;
  }
  .mug-image {
    position: absolute;
    left: 154px;
    top: 12px;
    width: 200px;
    height: 272px;
    border-radius: 10px 40px 14px 14px;
    background: linear-gradient(180deg, #fbf6e6 0%, #f6d45a 28%, #f2b31a 70%, #e5a012 100%);
    opacity: 0.9;
  }
  .wordmark {
    position: absolute;
    left: 100px;
    top: 117px;
    font-family: "Barlow Condensed", sans-serif;
    font-weight: 600;
    color: var(--ink);
    line-height: 1;
  }
  .wordmark__top { display: block; font-size: 40px; }
  .wordmark__bottom { display: block; font-size: 22px; letter-spacing: 0.5px; margin-top: 2px; }
  .holder-name {
    position: absolute;
    left: 33px;
    top: 46px;
    margin: 0;
    font-family: "Barlow Condensed", sans-serif;
    font-weight: 700;
    font-size: 31px;
    color: var(--ink);
    line-height: 1;
  }
  .holder-title {
    position: absolute;
    left: 33px;
    top: 80px;
    margin: 0;
    font-family: "Quicksand", sans-serif;
    font-weight: 400;
    font-size: 19px;
    letter-spacing: 1.2px;
    color: var(--ink-soft);
    line-height: 1;
  }
  .contact-list {
    position: absolute;
    left: 33px;
    top: 141px;
    margin: 0;
    padding: 0;
    list-style: none;
  }
  .contact-list__item {
    display: flex;
    align-items: center;
    height: 29.5px;
    font-family: "Barlow Condensed", sans-serif;
    font-weight: 500;
    font-size: 17px;
    color: var(--ink);
  }
  .contact-list__icon {
    width: 25px;
    height: 25px;
    margin-right: 11px;
    flex: none;
  }
</style>
</head>
<body>
<main class="canvas">
  <div class="side-label side-label--back">BACK</div>
  <div class="side-label side-label--front">FRONT</div>

  <section class="card card--back" aria-label="Card back">
    <svg class="card-shapes" viewBox="0 0 558 309" aria-hidden="true">
      <defs>
        <linearGradient id="goldBack" x1="0" x2="1" y1="0" y2="0">
          <stop offset="0" stop-color="var(--gold-3)"/>
          <stop offset="0.5" stop-color="var(--gold-2)"/>
          <stop offset="1" stop-color="var(--gold-1)"/>
        </linearGradient>
      </defs>
      <polygon points="286,46 297,46 338,82 558,82 558,92 332,92" fill="url(#goldBack)"/>
      <polygon points="0,228 214,228 214,237 0,237" fill="url(#goldBack)"/>
      <polygon points="262,262 272,262 290,276 425,276 420,285 283,285" fill="url(#goldBack)"/>
    </svg>
    <div class="mug-image" role="img" aria-label="Photo of a frothy mug of golden craft beer"></div>
    <div class="wordmark">
      <span class="wordmark__top">Roving</span>
      <span class="wordmark__bottom">HOPS GUY</span>
    </div>
  </section>

  <section class="card card--front" aria-label="Card front">
    <svg class="card-shapes" viewBox="0 0 558 309" aria-hidden="true">
      <defs>
        <linearGradient id="goldFront" x1="0" x2="1" y1="0" y2="0">
          <stop offset="0" stop-color="var(--gold-1)"/>
          <stop offset="0.5" stop-color="var(--gold-2)"/>
          <stop offset="1" stop-color="var(--gold-3)"/>
        </linearGradient>
        <linearGradient id="darkFront" x1="0" x2="1" y1="0" y2="1">
          <stop offset="0" stop-color="var(--dark-band-2)"/>
          <stop offset="1" stop-color="var(--dark-band)"/>
        </linearGradient>
      </defs>
      <polygon points="0,0 558,0 558,22 238,22 228,14 0,14" fill="var(--shade)" opacity="0.7"/>
      <polygon points="322,47 558,47 558,112 381,112" fill="url(#darkFront)"/>
      <polygon points="322,47 330,47 380,104 374,104" fill="url(#goldFront)"/>
      <polyline points="340,50 388,98 558,98" fill="none" stroke="url(#goldFront)" stroke-width="3"/>
      <polygon points="372,209 558,209 558,235 348,235" fill="var(--shade)" opacity="0.8"/>
      <polygon points="0,292 228,292 276,246 558,246 558,309 0,309" fill="url(#darkFront)"/>
      <polyline points="0,290 230,290 276,253 442,253" fill="none" stroke="url(#goldFront)" stroke-width="3"/>
    </svg>
    <h1 class="holder-name">Dale Corwin</h1>
    <p class="holder-title">Founder- Roving Hops Guy</p>
    <ul class="contact-list">
      <li class="contact-list__item">
        <svg class="contact-list__icon" viewBox="0 0 24 24" aria-hidden="true">
          <circle cx="12" cy="12" r="12" fill="var(--icon)"/>
          <path d="M8.2 6.2l2 2.3-1.1 1.4c.8 1.8 2.1 3.1 3.9 3.9l1.4-1.1 2.3 2-1.2 1.9c-4.3-.5-8.1-4.3-8.6-8.6z" fill="#fff"/>
        </svg>
        Business Telephone
      </li>
      <li class="contact-list__item">
        <svg class="contact-list__icon" viewBox="0 0 24 24" aria-hidden="true">
          <circle cx="12" cy="12" r="12" fill="var(--icon)"/>
          <text x="12" y="16.5" text-anchor="middle" font-family="Barlow Condensed, sans-serif" font-size="14" font-weight="600" fill="#fff">@</text>
        </svg>
        Dale@PineRidgeTraders.example
      </li>
      <li class="contact-list__item">
        <svg class="contact-list__icon" viewBox="0 0 24 24" aria-hidden="true">
          <circle cx="12" cy="12" r="12" fill="var(--icon)"/>
        </svg>
        @RovingHopsGuy
      </li>
      <li class="contact-list__item">
        <svg class="contact-list__icon" viewBox="0 0 24 24" aria-hidden="true">
          <circle cx="12" cy="12" r="12" fill="var(--icon)"/>
          <circle cx="12" cy="12" r="6.5" fill="none" stroke="#fff" stroke-width="1.4"/>
          <ellipse cx="12" cy="12" rx="2.8" ry="6.5" fill="none" stroke="#fff" stroke-width="1.2"/>
          <line x1="5.5" y1="12" x2="18.5" y2="12" stroke="#fff" stroke-width="1.2"/>
        </svg>
        www.Pineridgetraders.example
      </li>
    </ul>
  </section>
</main>
</body>
</html>
```